Australian Civil Construction, Quarry & Mining Services needs a business card

We need a business card designed for our Civil Construction, Quarry & Mining Services based in the country in Australia.
Our Company Brackley Earthworks provide innovate solutions for infrastructure, agricultural and mining (aggregate, sand, roadbase) industry.
We would like our business cards to be double sided
Front of card: black background or something that resembles our business colours. (it doesn't have to be black we are open to options)
- Company name - Brackley Earthworks
- Either our logo or some sort of icon/picture that resembles our business
- Website - https://brackleyearthworks.com.au/
- We will have a number of different names, positions descriptions, phone numbers and emails on separate cards for each of our managers/directors

```html
<!DOCTYPE html>
<html lang="en">
<head>
<meta charset="utf-8">
<title>Brackley Earthworks – Business Card</title>
<link href="https://fonts.googleapis.com/css2?family=Questrial&family=Roboto:wght@900&display=swap" rel="stylesheet">
<style>
  :root {
    --stage: #2a2a2a;
    --card: #221f20;
    --orange: #f5821f;
    --orange-deep: #b85a22;
    --ink-dark: #2a1a10;
    --white: #ffffff;
    --grey: #d9d9d9;
  }
  * { margin: 0; padding: 0; box-sizing: border-box; }
  html, body { width: 1200px; height: 481px; overflow: hidden; }
  body { background: var(--stage); position: relative; font-family: "Questrial", sans-serif; }

  .card {
    position: absolute; top: 101px; width: 464px; height: 279px;
    background: var(--card); overflow: hidden;
  }
  .card--front { left: 110px; }
  .card--back { left: 627px; }

  .site-photo {
    position: absolute; left: 0; right: 0; top: 120px; bottom: 0;
    background: linear-gradient(180deg, rgba(60,58,58,0) 0%, rgba(60,58,58,.45) 45%, rgba(30,28,28,.2) 100%);
  }
  .accent-panel { position: absolute; top: 0; height: 100%; }
  .card--front .accent-panel { left: 0; width: 250px; }
  .card--back .accent-panel { right: 0; width: 245px; }

  .front-mark {
    position: absolute; left: 306px; top: 78px; width: 66px; height: 66px;
    border-radius: 50%; background: var(--orange);
  }
  .front-name {
    position: absolute; left: 250px; width: 214px; top: 190px;
    text-align: center; font-family: "Roboto", sans-serif; font-weight: 900;
    font-size: 16px; line-height: 17px; letter-spacing: .4px; color: var(--grey);
    text-transform: uppercase;
  }

  .back-brand {
    position: absolute; left: 33px; top: 58px; display: flex; align-items: center; gap: 7px;
    font-size: 13px; color: var(--orange);
  }
  .back-brand .mark { width: 14px; height: 14px; background: var(--orange); }

  .name-bar {
    position: absolute; left: 92px; top: 132px; width: 190px; height: 21px;
    background: linear-gradient(90deg, var(--orange), var(--orange-deep));
    border-radius: 4px 0 0 4px;
  }
  .person {
    position: absolute; left: 32px; top: 131px; font-size: 22px; line-height: 22px;
    font-weight: 400; letter-spacing: -.3px; color: var(--white);
  }
  .person .surname { color: var(--ink-dark); margin-left: 6px; }
  .role { position: absolute; left: 32px; top: 155px; font-size: 13px; color: var(--white); }

  .contacts { position: absolute; left: 32px; top: 175px; list-style: none; }
  .contacts li { font-size: 13px; line-height: 17px; color: var(--white); white-space: nowrap; }
  .contacts .label { color: var(--orange); display: inline-block; width: 20px; }
</style>
</head>
<body>

<section class="card card--front">
  <div class="site-photo" role="img" aria-label="Faded photo of an earthworks site"></div>
  <svg class="accent-panel" viewBox="0 0 250 279" aria-hidden="true">
    <defs>
      <linearGradient id="frontGrad" x1="0" y1="0" x2="1" y2="1">
        <stop offset="0" stop-color="#b85a22"/>
        <stop offset=".55" stop-color="#f5821f"/>
        <stop offset="1" stop-color="#e2701d"/>
      </linearGradient>
    </defs>
    <polygon points="0,0 150,0 250,150 250,279 0,279" fill="url(#frontGrad)"/>
  </svg>
  <div class="front-mark" aria-hidden="true"></div>
  <h1 class="front-name">Brackley<br>Earthworks</h1>
</section>

<section class="card card--back">
  <div class="site-photo" role="img" aria-label="Faded photo of an earthworks site"></div>
  <svg class="accent-panel" viewBox="0 0 245 279" aria-hidden="true">
    <defs>
      <linearGradient id="backGrad" x1="1" y1="0" x2="0" y2="1">
        <stop offset="0" stop-color="#f5821f"/>
        <stop offset=".5" stop-color="#f5821f"/>
        <stop offset="1" stop-color="#b85a22"/>
      </linearGradient>
    </defs>
    <polygon points="100,0 245,0 245,279 30,279 0,220 0,180" fill="url(#backGrad)"/>
  </svg>

  <div class="back-brand"><span class="mark"></span><span>Brackley Earthworks</span></div>

  <div class="name-bar"></div>
  <h2 class="person">JOHN<span class="surname">DOE</span></h2>
  <p class="role">Manager</p>
  <ul class="contacts">
    <li><span class="label">C :</span>0400-517-284</li>
    <li><span class="label">E :</span>info@brackleyearthworks.com</li>
    <li><span class="label">W :</span>brackleyearthworks.com.au</li>
  </ul>
</section>

</body>
</html>
```